Harbourline Accountants needs a stationery design

We need a stationery design for our new innovative accountancy practise - it is to look professional and reliable but also minimalist, crisp, innovative and fresh. Avoid the use of block colour. You must include letterhead.

We look after business clients and help them get started and grow to successful companies. We provide a range of software, accounting, taxation and business consulting services to these clients.

This is a spin off from our more traditional existing practise - we would like to use the same green and blue.

The final design should communicate professional expertise coupled with innovative technology and personal care. The font of the type should reflect this - so far we have received standard font only.

We need business cards, letterhead, with comp slips, We need to see the whole set to form a view, not just the businesscard

I have uploaded the colours that we want to use from our existing letterhead, being the green and blue. We need to use the QFA logo - also enclosed - please use the text from the enclosed letterhead, but don't refer to this for design purposes - this was our temporary draft only.

Target Market(s)

Small to medium companies, high wealth investor clients

Industry/Entity Type

Professional Service

Requirements
Must have
• Crisp, simple design but evoking innovation, technology, competence and difference.
• So far the designs are too standard and not showing innovation.

```html
<!DOCTYPE html>
<html lang="en">
<head>
<meta charset="utf-8">
<title>Harbourline Accountants – Stationery Set</title>
<link href="https://fonts.googleapis.com/css2?family=PT+Sans:wght@400;700&family=Arimo:wght@400;700&family=Montserrat:wght@400;500&display=swap" rel="stylesheet">
<style>
:root{
  --bg:#dcdcdc;
  --paper:#ffffff;
  --green:#76923c;
  --blue:#2f5b94;
  --band-blue:#3b65a0;
  --navy:#24477a;
  --ink:#1a1a1a;
  --shadow:2px 3px 6px rgba(0,0,0,.35);
}
*{margin:0;padding:0;box-sizing:border-box}
html,body{width:1200px;height:1000px;overflow:hidden}
body{background:var(--bg);position:relative;font-family:"Arimo",Arial,sans-serif;color:var(--ink)}
.piece{position:absolute;background:var(--paper);box-shadow:var(--shadow);overflow:hidden}
.band{position:absolute;left:0;right:0;bottom:0;height:7px;display:flex}
.band span:first-child{flex:1;background:var(--band-blue)}
.band span:last-child{flex:1;background:var(--green)}
.brand{position:absolute;font-family:"PT Sans",sans-serif;text-align:center}
.brand .name{font-weight:700;color:var(--blue);white-space:nowrap;border-bottom:1px solid var(--blue);padding-bottom:1px;display:inline-block}
.brand .tag{color:var(--blue);margin-top:1px;white-space:nowrap}
.brand .tag b{font-weight:400;color:var(--green)}
.contact{position:absolute;font-family:"PT Sans",sans-serif;color:var(--blue);line-height:1.38}
.contact dt{float:left;clear:left;width:11px;color:var(--green);font-weight:700}
.contact dd{margin-left:12px;white-space:nowrap}
.label{position:absolute;font-family:"Montserrat",sans-serif;font-weight:500;font-size:25px;color:#111}
.assoc{position:absolute;font-family:"PT Sans",sans-serif;font-size:7px}
.assoc .mark{position:absolute;left:0;top:0;width:21px;height:21px;background:var(--navy)}
.assoc .line1{position:absolute;left:27px;top:14px;font-weight:700;white-space:nowrap}
.assoc .line2{position:absolute;left:0;top:26px;white-space:nowrap}
/* letterhead */
.letterhead{left:41px;top:35px;width:508px;height:717px}
.letterhead .brand{left:32px;top:26px}
.letterhead .brand .name{font-size:15px}
.letterhead .brand .tag{font-size:9px}
.rule-v{position:absolute;width:1px;background:var(--blue)}
.services{position:absolute;left:196px;top:27px;width:142px;text-align:center;font-family:"PT Sans",sans-serif;font-size:7px;line-height:1.3}
.services h4{color:var(--blue);font-size:8px;margin-bottom:2px}
.letter{position:absolute;left:34px;top:160px;width:452px;font-size:10.5px;line-height:13.6px}
.signature{position:absolute;left:34px;top:502px;width:80px;height:38px;background:linear-gradient(90deg,#f1f1f1,#e6e6e6)}
.closing{position:absolute;left:34px;top:545px;font-size:10.5px}
/* envelope */
.env-front{left:581px;top:35px;width:550px;height:274px}
.env-front .brand{left:21px;top:14px}
.env-back{left:584px;top:397px;width:553px;height:275px}
.env-back .brand{left:0;right:0;top:28px}
.env-back .brand .name{font-size:19px}
.env-back .brand .tag{font-size:11px}
.env-return{position:absolute;left:0;right:0;top:247px;text-align:center;font-family:"PT Sans",sans-serif;font-size:7px;color:var(--blue)}
.env-return b{color:var(--green)}
.flap{position:absolute;left:0;top:0}
/* comp slip */
.comp{left:43px;top:773px;width:426px;height:199px}
.comp .brand{left:17px;top:11px}
.comp-note{position:absolute;right:15px;top:170px;font-family:"PT Sans",sans-serif;font-weight:700;font-size:9px;color:var(--blue)}
.comp-note b{color:var(--green)}
/* cards */
.card-front{left:582px;top:732px;width:272px;height:162px}
.card-front .brand{left:13px;top:68px}
.card-front .brand .name{font-size:11.5px}
.card-front .brand .tag{font-size:7px}
.person{position:absolute;left:145px;top:48px;font-family:"PT Sans",sans-serif}
.person h3{font-size:10px;color:#111}
.person p{font-size:7px}
.card-services{position:absolute;left:145px;top:80px;font-family:"PT Sans",sans-serif;font-size:6.2px;color:var(--green);line-height:1.35;white-space:nowrap}
.card-services h4{color:var(--blue);font-size:6.8px}
.card-contact{position:absolute;right:12px;top:135px;text-align:right;font-family:"PT Sans",sans-serif;font-size:6px;color:var(--blue);line-height:1.5;white-space:nowrap}
.card-front .mini{position:absolute;left:14px;top:134px;width:15px;height:15px;background:var(--navy)}
.card-back{left:873px;top:732px;width:272px;height:162px;background:var(--navy);color:#fff}
.card-back .brand{left:0;right:0;top:55px}
.card-back .brand .name{color:#fff;border-color:#fff;font-size:14px}
.card-back .brand .tag{color:#fff;font-size:8.5px}
.card-back .foot{position:absolute;top:130px;font-family:"PT Sans",sans-serif;font-size:6px;line-height:1.4;white-space:nowrap}
</style>
</head>
<body>

<section class="piece letterhead">
  <div class="brand"><div class="name">Harbourline Accountants</div><div class="tag">Achieve with <b>Clarity</b></div></div>
  <div class="rule-v" style="left:190px;top:25px;height:33px"></div>
  <div class="services"><h4>Services:</h4>Taxation • Business Consulting • Software<br>Accounting • Bookkeeping</div>
  <div class="rule-v" style="left:338px;top:25px;height:33px"></div>
  <dl class="contact" style="left:357px;top:27px;font-size:7px">
    <dt>M:</dt><dd>0400 555 018</dd>
    <dt>T:</dt><dd>(02) 5550 1234</dd>
    <dt>E:</dt><dd>hello@harbourlineaccountants.com.au</dd>
    <dt>P:</dt><dd>P O Box 210, Kiama NSW 2533</dd>
    <dt>A:</dt><dd>ABN 12 345 678 901<br>Suite 4B, Level 1, 12 Shore Street,<br>Kiama NSW 2533</dd>
  </dl>
  <div class="letter">
    <p>August 28, 2011<br>First Last Name<br>Street Address<br>City, State 00000</p>
    <p style="margin:14px 0">Dear :</p>
    <p>Lorem ipsum dolor sit amet, consectetur adipiscing elit. Aenean ut ipsum eget massa hendrerit vestibulum vel in velit. Donec pretium neque velit.</p>
    <p>Aliquam porta lectus nec mauris ornare venenatis. Vivamus non est turpis, et cursus sem. Mauris vehicula erat in diam auctor at bibendum nisl lacinia.</p>
    <p>Morbi imperdiet neque vehicula nunc convallis gravida. Vestibulum iaculis pretium placerat. Integer consequat, est sit amet facilisis eleifend, nibh nibh varius orci, eget dapibus arcu dui non purus. Pellentesque in magna mauris. Duis enim sapien, dictum vitae condimentum a, pulvinar vel lacus. Mauris et molestie nibh. Vestibulum vitae nulla at metus elementum porta sit amet interdum elit. Nulla sollicitudin neque eu nulla volutpat congue.</p>
    <p>Etiam pellentesque, velit id dapibus fermentum, turpis sapien ornare dui, ac tincidunt ligula odio congue purus. Nunc sed ante dui, in porta lectus. Cras nec sem lorem. In hac habitasse platea dictumst. Maecenas id diam quis dui porta tristique. Sed id egestas felis. Donec ullamcorper mattis posuere. Phasellus fermentum eleifend tortor vel dapibus. Vestibulum ante ipsum.</p>
    <p>Etiam pellentesque, velit id dapibus fermentum, turpis sapien ornare dui, ac tincidunt ligula odio congue purus. Nunc sed ante dui, in porta lectus. Cras nec sem lorem. In hac habitasse platea dictumst. Maecenas id diam quis dui porta tristique. Sed id egestas felis. Donec ullamcorper mattis posuere. Phasellus fermentum eleifend tortor vel dapibus. Vestibulum ante ipsum.</p>
  </div>
  <div class="signature" role="img" aria-label="Handwritten signature"></div>
  <div class="closing">Sincerely,</div>
  <div class="assoc" style="left:34px;top:670px">
    <div class="mark" role="img" aria-label="Professional body badge"></div>
    <div class="line1">Harbourline Accountants is a QFA Practise</div>
    <div class="line2">Liability limited by a Scheme approved under Professional Standards Legislation</div>
  </div>
  <div class="band"><span></span><span></span></div>
</section>

<section class="piece env-front">
  <div class="brand"><div class="name" style="font-size:16px">Harbourline Accountants</div><div class="tag" style="font-size:9.5px">Achieve with <b>Clarity</b></div></div>
  <dl class="contact" style="left:357px;top:14px;font-size:7px">
    <dt>M:</dt><dd>0400 555 018</dd>
    <dt>T:</dt><dd>(02) 5550 1234</dd>
    <dt>E:</dt><dd>hello@harbourlineaccountants.com.au</dd>
    <dt>A:</dt><dd>ABN 12 345 678 901<br>Suite 4B, Level 1, 12 Shore Street, Kiama NSW 2533</dd>
  </dl>
  <div class="assoc" style="left:22px;top:226px">
    <div class="mark" role="img" aria-label="Professional body badge"></div>
    <div class="line1">Harbourline Accountants is a QFA Practise</div>
    <div class="line2">Liability limited by a Scheme approved under Professional Standards Legislation</div>
  </div>
  <div class="band" style="height:8px"><span></span><span></span></div>
</section>
<div class="label" style="left:787px;top:338px">Envelope</div>

<section class="piece env-back">
  <svg class="flap" width="553" height="110" viewBox="0 0 553 110" aria-hidden="true">
    <path d="M0 0 L10 0 C40 40 60 55 140 64 L276 80 L413 64 C493 55 513 40 543 0 L553 0" fill="#fff" stroke="#bdbdbd" stroke-width="1.2"/>
    <path d="M10 0 C40 40 60 55 140 64 L276 80 L413 64 C493 55 513 40 543 0" fill="none" stroke="rgba(0,0,0,.08)" stroke-width="4" transform="translate(0,2)"/>
  </svg>
  <div class="brand"><div class="name">Harbourline Accountants</div><div class="tag">Achieve with <b>Clarity</b></div></div>
  <div class="env-return"><b>P:</b> P O Box 210, Kiama NSW 2533</div>
  <div class="band" style="height:9px"><span></span><span></span></div>
</section>

<section class="piece comp">
  <div class="brand"><div class="name" style="font-size:12.5px">Harbourline Accountants</div><div class="tag" style="font-size:7.5px">Achieve with <b>Clarity</b></div></div>
  <dl class="contact" style="left:268px;top:12px;font-size:5.6px">
    <dt>M:</dt><dd>0400 555 018</dd>
    <dt>T:</dt><dd>(02) 5550 1234</dd>
    <dt>E:</dt><dd>hello@harbourlineaccountants.com.au</dd>
    <dt>P:</dt><dd>P O Box 210, Kiama NSW 2533</dd>
    <dt>A:</dt><dd>ABN 12 345 678 901<br>Suite 4B, Level 1, 12 Shore Street, Kiama NSW 2533</dd>
  </dl>
  <div class="comp-note">With <b>Compliments</b></div>
  <div class="band"><span></span><span></span></div>
</section>
<div class="label" style="left:483px;top:950px">Comp Slip</div>

<section class="piece card-front">
  <div class="rule-v" style="left:138px;top:48px;height:18px;background:#111"></div>
  <div class="person"><h3>James R. Carter</h3><p>Consultant</p></div>
  <div class="brand"><div class="name">Harbourline Accountants</div><div class="tag">Achieve with <b>Clarity</b></div></div>
  <div class="rule-v" style="left:138px;top:80px;height:26px"></div>
  <div class="card-services"><h4>Services:</h4>Taxation • Business Consulting • Software<br>Software • Accounting • Bookkeeping</div>
  <div class="card-contact">☏ 0400 555 018 &nbsp; ☏ (02) 5550 1234<br>✉ hello@harbourlineaccountants.com.au</div>
  <div class="mini" role="img" aria-label="Professional body badge"></div>
  <div class="band"><span></span><span></span></div>
</section>

<section class="piece card-back">
  <div class="brand"><div class="name">Harbourline Accountants</div><div class="tag">Achieve with Clarity</div></div>
  <div class="foot" style="left:14px">ABN 12 345 678 901<br>Suite 4B, Level 1, 12 Shore Street,<br>Kiama NSW 2533</div>
  <div class="foot" style="right:14px;text-align:right">P O Box 210, Kiama NSW 2533<br>◎ Website name</div>
</section>
<div class="label" style="left:765px;top:919px">Visiting Card</div>

</body>
</html>
```